Bright Harbor Construction

We are a commercial construction company specializing in steel stud framing, drywall, taping and acoustical ceilings. We would like a company logo (Something that looks great and isnt boring) as we have not been able to come up with one. A modern looking card would definitely suit our personalities best
Updates

We would like to try and avoid using dark colors. I have learned from experience that dark colors are the last to looked at. Thank you

```html
<!DOCTYPE html>
<html lang="en">
<head>
<meta charset="utf-8">
<title>Bright Harbor Construction – Business Card</title>
<link rel="stylesheet" href="https://fonts.googleapis.com/css2?family=Nunito+Sans:wght@400;700;800&family=Roboto:wght@400;500;700&display=swap">
<style>
  :root {
    --teal: #38a999;
    --teal-deep: #2f9a8b;
    --card: #ffffff;
    --ink: #58595b;
    --ink-soft: #6d6e70;
    --rule: #8a8a8a;
    --page: #ffffff;
  }
  * { box-sizing: border-box; margin: 0; padding: 0; }
  html, body {
    width: 1200px; height: 1139px; overflow: hidden;
    background: var(--page);
  }
  .stage {
    position: absolute; left: 3px; top: 25px;
    width: 1194px; height: 1100px;
    background: var(--teal);
  }
  .card {
    position: absolute; left: 240px; width: 692px;
    background: var(--card);
    border-radius: 34px;
    box-shadow: 0 18px 40px rgba(20, 80, 70, 0.35);
  }
  .card--front { top: 125px; height: 406px; }
  .card--back  { top: 603px; height: 408px; }

  .tab {
    position: absolute; left: 156px; width: 371px; height: 6px;
    background: var(--teal);
  }
  .tab--top { top: 0; border-radius: 0 0 3px 3px; }
  .tab--bottom { bottom: 0; border-radius: 3px 3px 0 0; }

  .front__mark {
    position: absolute; left: 292px; top: 114px;
    width: 108px; height: 108px; border-radius: 50%;
    background: var(--teal);
  }
  .front__name {
    position: absolute; left: 0; right: 0; top: 258px;
    text-align: center;
    font-family: "Nunito Sans", sans-serif; font-weight: 800;
    font-size: 38px; color: var(--ink); letter-spacing: 0.3px;
  }
  .front__tagline {
    position: absolute; left: 0; right: 0; top: 312px;
    text-align: center;
    font-family: "Nunito Sans", sans-serif; font-weight: 400;
    font-size: 17px; color: var(--ink); letter-spacing: 1.5px;
  }

  .back__brand {
    position: absolute; left: 52px; top: 154px; width: 210px;
    text-align: center;
    font-family: "Nunito Sans", sans-serif; font-weight: 700;
    font-size: 34px; line-height: 1.05; color: var(--teal);
  }
  .back__divider {
    position: absolute; left: 298px; top: 120px;
    width: 3px; height: 187px; background: var(--rule);
  }
  .back__person {
    position: absolute; left: 331px; top: 98px;
    font-family: "Roboto", sans-serif;
  }
  .person__name {
    font-weight: 700; font-size: 25px; color: var(--ink);
    letter-spacing: -0.2px;
  }
  .person__role {
    margin-top: 3px; font-size: 16px; color: var(--ink-soft);
  }
  .contact {
    position: absolute; left: 337px; top: 185px;
    list-style: none;
    font-family: "Roboto", sans-serif; font-size: 16px; color: var(--ink-soft);
  }
  .contact__item {
    display: flex; align-items: center; height: 33px;
  }
  .contact__icon {
    width: 16px; height: 16px; margin-right: 13px; flex: none;
    fill: var(--teal-deep);
  }
</style>
</head>
<body>
  <main class="stage">
    <section class="card card--front" aria-label="Card front">
      <span class="tab tab--top"></span>
      <span class="front__mark"></span>
      <h1 class="front__name">Bright Harbor</h1>
      <p class="front__tagline">CONSTRUCTION</p>
      <span class="tab tab--bottom"></span>
    </section>

    <section class="card card--back" aria-label="Card back">
      <p class="back__brand">Bright<br>Harbor</p>
      <span class="back__divider"></span>
      <div class="back__person">
        <h2 class="person__name">YOR NAME HERE</h2>
        <p class="person__role">Designation</p>
      </div>
      <ul class="contact">
        <li class="contact__item">
          <svg class="contact__icon" viewBox="0 0 24 24" aria-hidden="true"><path d="M6.6 10.8c1.4 2.8 3.8 5.1 6.6 6.6l2.2-2.2c.3-.3.7-.4 1-.2 1.1.4 2.3.6 3.6.6.6 0 1 .4 1 1V20c0 .6-.4 1-1 1C10.6 21 3 13.4 3 4c0-.6.4-1 1-1h3.5c.6 0 1 .4 1 1 0 1.3.2 2.5.6 3.6.1.3 0 .7-.2 1l-2.3 2.2z"/></svg>
          XXX-XXX-XXXX
        </li>
        <li class="contact__item">
          <svg class="contact__icon" viewBox="0 0 24 24" aria-hidden="true"><path d="M3 5h18v14H3z M4.5 6.5v.4l7.5 5 7.5-5v-.4z" fill-rule="evenodd"/></svg>
          name@brightharbor.com
        </li>
        <li class="contact__item">
          <svg class="contact__icon" viewBox="0 0 24 24" aria-hidden="true"><circle cx="12" cy="12" r="10"/><path d="M2 12h20M12 2c3 3 3 17 0 20M12 2c-3 3-3 17 0 20" stroke="#fff" stroke-width="1.5" fill="none"/></svg>
          brightharbor.com
        </li>
        <li class="contact__item">
          <svg class="contact__icon" viewBox="0 0 24 24" aria-hidden="true"><path d="M12 2a7 7 0 0 0-7 7c0 5.2 7 13 7 13s7-7.8 7-13a7 7 0 0 0-7-7zm0 9.5a2.5 2.5 0 1 1 0-5 2.5 2.5 0 0 1 0 5z"/></svg>
          Your adress here
        </li>
      </ul>
    </section>
  </main>
</body>
</html>
```